Wine label refresh

We are wanting to modify our Corran Estate label to include a picture on it.
I have attached the pictures below which we would like on the label. They are of the Corran Estate vineyard. I have also attached an example of another label with a picture on it that we like the style of.
Industry/Entity Type
Vineyard
Requirements
Must have
- The Corran Estate text must stay the same but can be moved down. It still needs to be the same size though.
Marlborough Sauvignon Blanc should remain in the same font and roughly the same size.
Wine of New Zealand also must stay but could potentially be moved.
Nice to have
- It would be nice if we could keep the KL logo on the front label but feel free to experiment with where this goes.

```html
<!DOCTYPE html>
<html lang="en">
<head>
<meta charset="utf-8">
<title>Corran Estate – Marlborough Sauvignon Blanc 2013</title>
<link rel="stylesheet" href="https://fonts.googleapis.com/css2?family=Cormorant+SC:wght@500&family=Pinyon+Script&family=Caladea&display=swap">
<style>
  :root {
    --paper: #ffffff;
    --ink: #1b1b1b;
    --frame: #222222;
    --band: #f0a81a;
    --band-edge: #d48f10;
    --sky: #9ea3a8;
    --hills: #7f9563;
    --vines: #4f7d33;
  }
  * { margin: 0; padding: 0; box-sizing: border-box; }
  html, body {
    width: 1025px;
    height: 1200px;
    overflow: hidden;
    background: var(--paper);
  }
  .label {
    position: relative;
    width: 1025px;
    height: 1200px;
    background: var(--paper);
    color: var(--ink);
  }
  .label-card {
    position: absolute;
    left: 45px;
    top: 43px;
    width: 937px;
    height: 1126px;
    background: var(--paper);
    border: 2px solid var(--frame);
    box-shadow: 3px 4px 6px rgba(0, 0, 0, 0.35);
  }
  .brand-initials {
    position: absolute;
    left: 0;
    width: 1025px;
    top: 92px;
    text-align: center;
    font-family: "Cormorant SC", serif;
    font-weight: 500;
    font-size: 100px;
    letter-spacing: 4px;
    line-height: 1;
  }
  .estate-name {
    position: absolute;
    left: 0;
    width: 1025px;
    top: 240px;
    text-align: center;
    font-family: "Cormorant SC", serif;
    font-weight: 500;
    font-size: 80px;
    letter-spacing: 3px;
    line-height: 1;
  }
  .vineyard-photo {
    position: absolute;
    left: 69px;
    top: 380px;
    width: 897px;
    height: 276px;
    display: block;
  }
  .variety-band {
    position: absolute;
    left: 0;
    top: 706px;
    width: 1025px;
    height: 312px;
    background: var(--band);
    border-top: 1px solid var(--band-edge);
    border-bottom: 1px solid var(--band-edge);
    box-shadow: 0 3px 6px rgba(0, 0, 0, 0.4);
  }
  .variety-name {
    position: absolute;
    left: 0;
    width: 1025px;
    top: 44px;
    text-align: center;
    font-family: "Pinyon Script", cursive;
    font-weight: 400;
    font-size: 80px;
    line-height: 1.2;
    white-space: nowrap;
  }
  .vintage {
    position: absolute;
    left: 0;
    width: 1025px;
    top: 196px;
    text-align: center;
    font-family: "Pinyon Script", cursive;
    font-size: 50px;
    line-height: 1.2;
  }
  .origin {
    position: absolute;
    left: 0;
    width: 1025px;
    top: 1030px;
    text-align: center;
    font-family: "Pinyon Script", cursive;
    font-size: 82px;
    line-height: 1.2;
  }
  .spec {
    position: absolute;
    top: 1108px;
    font-family: "Caladea", serif;
    font-size: 33px;
    line-height: 1;
  }
  .spec-volume { left: 68px; }
  .spec-abv { right: 61px; }
</style>
</head>
<body>
  <main class="label">
    <div class="label-card"></div>

    <p class="brand-initials">KL</p>
    <h1 class="estate-name">Corran Estate</h1>

    <svg class="vineyard-photo" viewBox="0 0 897 276" role="img" aria-label="Photograph of the Corran Estate vineyard: rows of vines leading to a cottage and palm trees beneath green hills and an overcast sky">
      <defs>
        <linearGradient id="vineyard-tones" x1="0" y1="0" x2="0" y2="1">
          <stop offset="0" stop-color="var(--sky)"/>
          <stop offset="0.3" stop-color="#b8bcbf"/>
          <stop offset="0.45" stop-color="var(--hills)"/>
          <stop offset="0.75" stop-color="var(--vines)"/>
          <stop offset="1" stop-color="#6a9a40"/>
        </linearGradient>
      </defs>
      <rect width="897" height="276" fill="url(#vineyard-tones)"/>
    </svg>

    <section class="variety-band">
      <h2 class="variety-name">Marlborogh Sauvignon Blanc</h2>
      <p class="vintage">2013</p>
    </section>

    <p class="origin">New Zealand</p>
    <p class="spec spec-volume">750ml</p>
    <p class="spec spec-abv">13% Alc/Vol</p>
  </main>
</body>
</html>
```